App UI design needed! For a Password Management Tool

Need a design of a Windows desktop application which is a Password Management Tool, similar to Vaultkin, Brimlock or Keywell, with Business/Enterprise functionalities. Here attached are a few sample pages of Brimlock, and some sample pages of our app called Tessaly. We certainly want to redesign our app.
We need: 1. The layout of the web: top banner, menu, main pane; 2. Form style, main form and sub forms; 3. List style; 4 Fonts and buttons; 5. Logo.
The design should look professional, can attract business customers as well as individual users, and present a strong sense of “Security”. The look and feel should differentiate from well-known products like Vaultkin, Brimlock, Keywell, etc.

```html
<!DOCTYPE html>
<html lang="en">
<head>
<meta charset="utf-8">
<title>Tessaly – Password Manager Screens</title>
<link href="https://fonts.googleapis.com/css2?family=Poppins:wght@400;500;600&display=swap" rel="stylesheet">
<style>
:root{
  --page:#ffffff;
  --logo-bg:#1d2025;
  --header:#22252a;
  --sidebar:#25282d;
  --main:#2b2e34;
  --list-bg:#24272c;
  --table-head:#1b1d20;
  --row:#26292e;
  --row-dark:#1c1e22;
  --modal:#17191c;
  --line:#3a3d43;
  --text:#ffffff;
  --muted:#c9ccd1;
  --blue:#1e8fe6;
  --blue-deep:#1a7bd1;
  --gold:#f2b705;
}
*{box-sizing:border-box;margin:0;padding:0}
html,body{width:1200px;height:707px;overflow:hidden;background:var(--page)}
body{position:relative;font-family:'Poppins',sans-serif;color:var(--text)}
.frame{position:absolute;width:560px;height:315px;overflow:hidden}
.screen{position:absolute;left:0;top:0;width:1171px;height:658px;transform:scale(.4785);transform-origin:0 0;background:var(--main)}
.abs{position:absolute}
.logo-area{position:absolute;left:0;top:0;width:202px;height:67px;background:var(--logo-bg);display:flex;align-items:center;justify-content:center;gap:8px}
.logo-dot{width:18px;height:18px;border-radius:50%;background:var(--blue)}
.logo-name{font-size:19px;font-weight:500;color:var(--blue)}
.topbar{position:absolute;left:202px;top:0;right:0;height:67px;background:var(--header)}
.round-btn{position:absolute;width:26px;height:26px;border-radius:50%;border:1.5px solid #d7d9dc;display:flex;align-items:center;justify-content:center}
.avatar{position:absolute;width:26px;height:26px;border-radius:50%;background:var(--blue);display:flex;align-items:center;justify-content:center}
.welcome{position:absolute;font-size:11.5px;line-height:14px}
.welcome b{font-weight:600}
.sidebar{position:absolute;left:0;top:67px;width:202px;bottom:0;background:var(--sidebar)}
.nav-item{position:absolute;left:0;width:202px;height:34px;display:flex;align-items:center;padding-left:12px;gap:12px;font-size:11.5px;font-weight:600;border-bottom:1px solid #34373d}
.nav-item svg{width:14px;height:14px}
.nav-item.sub{padding-left:38px;border-bottom:none}
.nav-item.sub span.hash{font-weight:600;margin-right:4px}
.nav-item.active{left:8px;width:194px;height:44px;background:var(--blue);border-radius:22px 0 0 22px;border:none;padding-left:28px}
.title{position:absolute;left:268px;top:84px;font-size:20px;font-weight:500}
.rule{position:absolute;left:268px;top:126px;width:877px;height:1px;background:var(--line)}
.search{position:absolute;height:32px;border:1px solid #8b8f96;background:#25282d;font-size:12px;padding:0 9px;display:flex;align-items:center;justify-content:space-between;color:#e0e2e5}
.btn-new{position:absolute;height:32px;width:76px;border:1px solid var(--blue);color:var(--blue);font-size:12px;display:flex;align-items:center;justify-content:center}
.table{position:absolute;border:1px solid #3a3d43}
.thead{position:absolute;left:0;right:0;top:0;height:46px;background:var(--table-head);font-size:13.5px;font-weight:600}
.row{position:absolute;left:0;right:0;background:var(--row);border-top:1px solid #383b41;font-size:14px}
.row.dark{background:var(--row-dark)}
.cell{position:absolute;top:50%;transform:translateY(-50%);white-space:nowrap}
.ring{position:absolute;width:32px;height:32px;border-radius:50%;border:1.5px solid var(--blue);display:flex;align-items:center;justify-content:center;color:var(--blue);font-weight:600;font-size:15px}
.ring svg{width:16px;height:16px}
.count{position:absolute;right:13px;bottom:11px;font-size:11px;color:#e4e6e9}
/* detail view */
.list-pane{position:absolute;left:269px;top:126px;width:379px;bottom:0;background:var(--list-bg)}
.list-item{position:absolute;left:10px;font-size:11.5px}
.card{position:absolute;left:666px;width:479px;border:1px solid #3a3d43;background:#282b30}
.card .label{position:absolute;left:14px;font-size:11px;color:#e5e7ea}
.card .value{position:absolute;left:14px;font-size:13.5px;font-weight:600}
/* modal */
.modal{position:absolute;left:679px;top:86px;width:492px;height:572px;background:var(--modal)}
.modal-head{position:absolute;left:0;top:0;right:0;height:40px;background:var(--blue-deep);font-size:14px;font-weight:500;padding:0 14px;display:flex;align-items:center;justify-content:space-between}
.field-label{position:absolute;font-size:12px;color:#eceef0}
.input{position:absolute;height:34px;background:#fff;border:1px solid #cfd2d6}
.tab{position:absolute;font-size:12px;font-weight:500}
.radio{position:absolute;font-size:12px;display:flex;align-items:center;gap:5px}
.radio i{display:block;width:10px;height:10px;border-radius:50%;background:#fff}
.mini-table{position:absolute;left:697px;top:445px;width:379px;height:91px;border:1px solid #4a4d53;background:#202226;font-size:11px}
.btn{position:absolute;height:32px;width:76px;display:flex;align-items:center;justify-content:center;font-size:12.5px;border:1px solid #c9ccd1}
.btn.save{border-color:var(--blue);color:var(--blue)}
.stamp{position:absolute;left:697px;font-size:11.5px;color:#e9ebee}
</style>
</head>
<body>

<svg width="0" height="0" style="position:absolute">
  <defs>
    <symbol id="i-search" viewBox="0 0 16 16"><circle cx="7" cy="7" r="4.5" fill="none" stroke="currentColor" stroke-width="2"/><path d="M10.3 10.3 14 14" stroke="currentColor" stroke-width="2.2" stroke-linecap="round"/></symbol>
    <symbol id="i-mail" viewBox="0 0 16 16"><rect x="2" y="4" width="12" height="8" rx="1" fill="currentColor"/><path d="M2 4.5 8 9l6-4.5" fill="none" stroke="#22252a" stroke-width="1.2"/></symbol>
    <symbol id="i-user" viewBox="0 0 16 16"><circle cx="8" cy="5" r="3.2" fill="currentColor"/><path d="M2 15c0-3.6 2.7-5.5 6-5.5s6 1.9 6 5.5z" fill="currentColor"/></symbol>
    <symbol id="i-team" viewBox="0 0 16 16"><circle cx="8" cy="6" r="2.4" fill="currentColor"/><circle cx="3.5" cy="7" r="1.8" fill="currentColor"/><circle cx="12.5" cy="7" r="1.8" fill="currentColor"/><path d="M3.5 14c0-3 2-4.3 4.5-4.3s4.5 1.3 4.5 4.3zM0 14c0-2.2 1.3-3.4 3.2-3.4L3 14zM16 14c0-2.2-1.3-3.4-3.2-3.4L13 14z" fill="currentColor"/></symbol>
    <symbol id="i-gauge" viewBox="0 0 16 16"><path d="M1 12a7 7 0 0 1 14 0z" fill="currentColor"/><path d="M8 12 11 6" stroke="#25282d" stroke-width="1.6"/></symbol>
    <symbol id="i-flag" viewBox="0 0 16 16"><path d="M1 3l4.5-1.5 5 1.5L15 1.5v10L10.5 13l-5-1.5L1 13z" fill="currentColor"/></symbol>
    <symbol id="i-laptop" viewBox="0 0 16 16"><rect x="3" y="3" width="10" height="7" fill="none" stroke="currentColor" stroke-width="1.6"/><rect x="1" y="11" width="14" height="2" fill="currentColor"/></symbol>
    <symbol id="i-chart" viewBox="0 0 16 16"><path d="M7 2a6.5 6.5 0 1 0 6.5 6.5H7z" fill="currentColor"/><path d="M9 1v6h6A6 6 0 0 0 9 1z" fill="currentColor"/></symbol>
    <symbol id="i-star" viewBox="0 0 16 16"><path d="M8 1l2.1 4.6 5 .5-3.8 3.3 1.1 4.9L8 11.8l-4.4 2.5 1.1-4.9L.9 6.1l5-.5z" fill="currentColor"/></symbol>
    <symbol id="i-key" viewBox="0 0 16 16"><circle cx="11" cy="5" r="3.6" fill="currentColor"/><path d="M8.5 7.5 2 14" stroke="currentColor" stroke-width="2.4" stroke-linecap="round"/><path d="M4 12l1.8 1.8" stroke="currentColor" stroke-width="1.8"/></symbol>
    <symbol id="i-tag" viewBox="0 0 16 16"><path d="M1 2v6l7 7 7-7-7-7H2z" fill="currentColor"/><circle cx="4.5" cy="4.5" r="1.3" fill="#25282d"/></symbol>
    <symbol id="i-pencil" viewBox="0 0 16 16"><path d="M2 14l1-4 8-8 3 3-8 8z" fill="currentColor"/></symbol>
    <symbol id="i-trash" viewBox="0 0 16 16"><rect x="3" y="2" width="10" height="2" fill="currentColor"/><path d="M4 5h8l-1 10H5z" fill="currentColor"/></symbol>
  </defs>
</svg>

<!-- Screen 1: Client Containers -->
<div class="frame" style="left:30px;top:24px">
  <div class="screen">
    <div class="logo-area"><span class="logo-dot"></span><span class="logo-name">Tessaly</span></div>
    <div class="topbar"></div>
    <div class="round-btn" style="left:966px;top:18px"><svg width="12" height="12" color="#fff"><use href="#i-search"/></svg></div>
    <div class="round-btn" style="left:1004px;top:18px"><svg width="12" height="12" color="#fff"><use href="#i-mail"/></svg></div>
    <div class="avatar" style="left:1043px;top:18px"><svg width="13" height="13" color="#fff"><use href="#i-user"/></svg></div>
    <div class="welcome" style="left:1077px;top:17px">Welcome<br><b>User Name</b></div>
    <div class="sidebar">
      <div class="nav-item" style="top:10px"><svg color="#fff"><use href="#i-gauge"/></svg>Dashboard</div>
      <div class="nav-item" style="top:55px"><svg color="#fff"><use href="#i-user"/></svg>Users</div>
      <div class="nav-item" style="top:100px"><svg color="#fff"><use href="#i-team"/></svg>Team</div>
      <div class="nav-item active" style="top:141px"><svg color="#fff"><use href="#i-flag"/></svg>Client Containers</div>
      <div class="nav-item" style="top:191px"><svg color="#fff"><use href="#i-laptop"/></svg>Web Logins</div>
      <div class="nav-item" style="top:236px"><svg color="#fff"><use href="#i-chart"/></svg>Reports</div>
    </div>
    <div class="title">Client Containers</div>
    <div class="rule"></div>
    <div class="search" style="left:268px;top:145px;width:379px">Search<svg width="12" height="12" color="#fff"><use href="#i-search"/></svg></div>
    <div class="btn-new" style="left:658px;top:145px">+ New</div>
    <div class="table" style="left:268px;top:188px;width:877px;height:149px">
      <div class="thead">
        <span class="cell" style="left:18px">Client Containers Des...</span>
        <span class="cell" style="left:229px">IP</span>
        <span class="cell" style="left:440px">Remarks</span>
        <span class="cell" style="left:677px">Status</span>
      </div>
      <div class="row" style="top:46px;height:50px">
        <span class="cell" style="left:18px">Window China 65...</span>
        <span class="cell" style="left:229px">65.... 65.52.168.124</span>
        <span class="cell" style="left:440px">Clients-1</span>
        <span class="cell" style="left:677px">Active</span>
      </div>
      <div class="row" style="top:96px;height:52px">
        <span class="cell" style="left:18px">Window China 65...</span>
        <span class="cell" style="left:229px">65.... 65.52.168.124</span>
        <span class="cell" style="left:440px">Clients-2</span>
        <span class="cell" style="left:677px">Active</span>
      </div>
    </div>
    <div class="count">x10</div>
  </div>
</div>

<!-- Screen 2: Web Login detail -->
<div class="frame" style="left:609px;top:24px">
  <div class="screen">
    <div class="logo-area"><span class="logo-dot"></span><span class="logo-name">Tessaly</span></div>
    <div class="topbar"></div>
    <div class="round-btn" style="left:965px;top:20px"><svg width="12" height="12" color="#fff"><use href="#i-search"/></svg></div>
    <div class="round-btn" style="left:1003px;top:20px"><svg width="12" height="12" color="#fff"><use href="#i-mail"/></svg></div>
    <div class="avatar" style="left:1042px;top:20px"><svg width="13" height="13" color="#fff"><use href="#i-user"/></svg></div>
    <div class="welcome" style="left:1076px;top:19px">Welcome<br><b>User Name</b></div>
    <div class="sidebar">
      <div class="nav-item" style="top:9px"><svg color="var(--gold)"><use href="#i-star"/></svg>Favourites</div>
      <div class="nav-item" style="top:43px"><svg color="var(--gold)"><use href="#i-star"/></svg>KLVR</div>
      <div class="nav-item" style="top:77px"><svg color="var(--gold)"><use href="#i-key"/></svg>Web Logins</div>
      <div class="nav-item" style="top:120px;border:none"><svg color="var(--gold)"><use href="#i-tag"/></svg>Tags</div>
      <div class="nav-item sub" style="top:148px;height:28px"><span class="hash">#</span> Kelvara tag</div>
      <div class="nav-item sub" style="top:176px;height:28px"><span class="hash">#</span> News</div>
      <div class="nav-item sub" style="top:203px;height:28px"><span class="hash">#</span> Office</div>
      <div class="nav-item sub" style="top:231px;height:28px;border-bottom:1px solid #34373d"><span class="hash">#</span> Source code</div>
      <div class="nav-item" style="top:265px"><svg color="var(--gold)"><use href="#i-user"/></svg>Personal</div>
      <div class="nav-item" style="top:299px"><svg color="var(--gold)"><use href="#i-laptop"/></svg>Web Logins</div>
      <div class="nav-item" style="top:332px;border:none"><svg color="var(--gold)"><use href="#i-tag"/></svg>My Tags</div>
      <div class="nav-item sub" style="top:360px;height:28px;border-bottom:1px solid #34373d"><span class="hash">#</span> 你好</div>
      <div class="nav-item" style="top:394px;border:none"><span style="width:14px;color:var(--gold);font-weight:600;text-align:center">$</span>Payment</div>
    </div>
    <div class="title">Web Logins</div>
    <div class="list-pane">
      <div class="search" style="left:10px;top:19px;width:353px">Search<svg width="12" height="12" color="#fff"><use href="#i-search"/></svg></div>
      <div class="ring" style="left:10px;top:70px"><svg color="var(--blue)"><use href="#i-key"/></svg></div>
      <div class="list-item" style="left:58px;top:78px">exchange.kelvara my kelvara \ hana_gale</div>
      <div class="ring" style="left:10px;top:121px"></div>
      <div class="list-item" style="left:58px;top:129px">Chatterly jmarlow@mailpost.com</div>
      <div class="ring" style="left:10px;top:171px"></div>
      <div class="list-item" style="left:58px;top:179px">repodock jmarlow@mailpost.com</div>
      <div class="ring" style="left:10px;top:220px">i</div>
      <div class="list-item" style="left:58px;top:228px">talentry-default lena_gale@kelvara.com</div>
    </div>
    <div class="abs" style="left:1090px;top:143px;font-size:11.5px;display:flex;align-items:center;gap:4px"><svg width="11" height="11" color="#fff"><use href="#i-pencil"/></svg><span style="text-decoration:underline">Edit</span></div>
    <div class="abs" style="left:1140px;top:143px;font-size:13px;font-weight:600">⋮</div>
    <div class="abs" style="left:666px;top:191px;width:48px;height:48px;border-radius:50%;border:2px solid #3b7fc4"></div>
    <div class="abs" style="left:729px;top:194px;font-size:28px;font-weight:600">repodock</div>
    <div class="card" style="top:257px;height:96px">
      <div class="label" style="top:14px">Login User Name</div>
      <div class="value" style="top:31px">jmarlow@mailpost.com</div>
      <div class="abs" style="left:0;right:0;top:60px;height:1px;background:#3a3d43"></div>
      <div class="label" style="top:68px;color:var(--blue)">Login Password: ***********</div>
    </div>
    <div class="card" style="top:366px;height:61px">
      <div class="label" style="top:12px">Login Page URL</div>
      <div class="value" style="top:29px">https://repodock.com/Login</div>
    </div>
    <div class="card" style="top:439px;height:61px">
      <div class="label" style="top:12px">Client Container</div>
      <div class="value" style="top:29px">Windows-China-65.52.168.124</div>
    </div>
    <div class="count">x10</div>
  </div>
</div>

<!-- Screen 3: New Web Login form -->
<div class="frame" style="left:30px;top:355px">
  <div class="screen">
    <div class="logo-area"><span class="logo-dot"></span><span class="logo-name">Tessaly</span></div>
    <div class="topbar"></div>
    <div class="round-btn" style="left:965px;top:21px"><svg width="12" height="12" color="#fff"><use href="#i-search"/></svg></div>
    <div class="round-btn" style="left:1003px;top:21px"><svg width="12" height="12" color="#fff"><use href="#i-mail"/></svg></div>
    <div class="avatar" style="left:1042px;top:21px"><svg width="13" height="13" color="#fff"><use href="#i-user"/></svg></div>
    <div class="welcome" style="left:1076px;top:19px">Welcome<br><b>User Name</b></div>
    <div class="sidebar">
      <div class="nav-item" style="top:9px"><svg color="var(--gold)"><use href="#i-gauge"/></svg>Dashboard</div>
      <div class="nav-item" style="top:54px"><svg color="var(--gold)"><use href="#i-user"/></svg>Users</div>
      <div class="nav-item" style="top:100px"><svg color="var(--gold)"><use href="#i-team"/></svg>Team</div>
      <div class="nav-item" style="top:145px"><svg color="var(--gold)"><use href="#i-flag"/></svg>Client Containers</div>
      <div class="nav-item active" style="top:184px"><svg color="#fff"><use href="#i-laptop"/></svg>Web Logins</div>
      <div class="nav-item" style="top:234px"><svg color="var(--gold)"><use href="#i-chart"/></svg>Reports</div>
    </div>
    <div class="title">Web Logins</div>
    <div class="rule" style="width:420px"></div>
    <div class="search" style="left:268px;top:145px;width:379px">Search<svg width="12" height="12" color="#fff"><use href="#i-search"/></svg></div>
    <div class="btn-new" style="left:658px;top:145px"></div>
    <div class="table" style="left:268px;top:188px;width:877px;height:242px">
      <div class="thead">
        <span class="cell" style="left:18px">Name</span>
        <span class="cell" style="left:281px">Username</span>
      </div>
      <div class="row" style="top:46px;height:50px">
        <div class="ring" style="left:16px;top:9px"><svg color="var(--blue)"><use href="#i-key"/></svg></div>
        <span class="cell" style="left:70px">exchange.kelvara</span>
        <span class="cell" style="left:281px">my kelvara \ hana_gale</span>
      </div>
      <div class="row" style="top:96px;height:48px">
        <div class="ring" style="left:16px;top:8px"></div>
        <span class="cell" style="left:70px">Chatterly</span>
        <span class="cell" style="left:281px">jmarlow@mailpost.com</span>
      </div>
      <div class="row dark" style="top:144px;height:49px">
        <div class="ring" style="left:16px;top:8px"></div>
        <span class="cell" style="left:70px">Repodock</span>
        <span class="cell" style="left:281px">jmarlow@mailpost.com</span>
      </div>
      <div class="row" style="top:193px;height:48px">
        <div class="ring" style="left:16px;top:8px">i</div>
        <span class="cell" style="left:70px">talentry - default</span>
        <span class="cell" style="left:281px">lena_gale@kelvara.com</span>
      </div>
    </div>
    <div class="modal" style="left:679px;top:86px">
      <div class="modal-head"><span>Web Login</span><span style="font-size:12px">X</span></div>
    </div>
    <div class="field-label" style="left:697px;top:143px">Web Login Name*</div>
    <div class="input" style="left:697px;top:169px;width:448px"></div>
    <div class="field-label" style="left:697px;top:214px">Login Page URL*</div>
    <div class="input" style="left:697px;top:240px;width:448px"></div>
    <div class="field-label" style="left:697px;top:284px">User Name*</div>
    <div class="field-label" style="left:934px;top:284px">Password*</div>
    <div class="input" style="left:697px;top:309px;width:209px"></div>
    <div class="input" style="left:934px;top:309px;width:209px"></div>
    <div class="tab" style="left:712px;top:363px">Assign</div>
    <div class="tab" style="left:849px;top:363px">Bind A Client Container</div>
    <div class="abs" style="left:697px;top:388px;width:446px;height:1px;background:#6a6e75"></div>
    <div class="abs" style="left:697px;top:385px;width:72px;height:5px;background:var(--blue)"></div>
    <div class="radio" style="left:697px;top:412px"><i></i>Not Specified</div>
    <div class="radio" style="left:808px;top:412px"><i></i>Client Container</div>
    <div class="mini-table">
      <div class="abs" style="left:0;right:0;top:0;height:31px;background:var(--table-head);font-weight:600">
        <span class="cell" style="left:9px">Machine Description</span><span class="cell" style="left:220px">IP</span>
      </div>
      <div class="abs" style="left:0;right:0;top:35px;height:25px;background:#26292e">
        <span class="cell" style="left:9px">Window China 65...</span><span class="cell" style="left:220px">65.... 65.52.168.124</span>
      </div>
      <div class="abs" style="left:0;right:0;top:61px;height:25px">
        <span class="cell" style="left:9px">Window China 65...</span><span class="cell" style="left:220px">65.... 65.52.168.124</span>
      </div>
    </div>
    <div class="btn" style="left:697px;top:548px">Cancel</div>
    <div class="btn save" style="left:782px;top:548px">Save</div>
    <div class="stamp" style="top:594px">Created 2022-03-24 17:31:29 (GMT+08:00)</div>
    <div class="stamp" style="top:616px">Modified 2022-03-24 17:31:41 (GMT+08:00)</div>
  </div>
</div>

<!-- Screen 4: Web Logins list -->
<div class="frame" style="left:609px;top:355px">
  <div class="screen">
    <div class="logo-area"><span class="logo-dot"></span><span class="logo-name">Tessaly</span></div>
    <div class="topbar"></div>
    <div class="round-btn" style="left:965px;top:21px"><svg width="12" height="12" color="#fff"><use href="#i-search"/></svg></div>
    <div class="round-btn" style="left:1003px;top:21px"><svg width="12" height="12" color="#fff"><use href="#i-mail"/></svg></div>
    <div class="avatar" style="left:1042px;top:21px"><svg width="13" height="13" color="#fff"><use href="#i-user"/></svg></div>
    <div class="welcome" style="left:1076px;top:19px">Welcome<br><b>User Name</b></div>
    <div class="sidebar">
      <div class="nav-item" style="top:9px"><svg color="var(--gold)"><use href="#i-gauge"/></svg>Dashboard</div>
      <div class="nav-item" style="top:54px"><svg color="var(--gold)"><use href="#i-user"/></svg>Users</div>
      <div class="nav-item" style="top:100px"><svg color="var(--gold)"><use href="#i-team"/></svg>Team</div>
      <div class="nav-item" style="top:145px"><svg color="var(--gold)"><use href="#i-flag"/></svg>Client Containers</div>
      <div class="nav-item active" style="top:184px"><svg color="#fff"><use href="#i-laptop"/></svg>Web Logins</div>
      <div class="nav-item" style="top:234px"><svg color="var(--gold)"><use href="#i-chart"/></svg>Reports</div>
    </div>
    <div class="title" style="left:269px">Web Logins</div>
    <div class="rule" style="left:269px;width:876px"></div>
    <div class="search" style="left:269px;top:145px;width:378px">Search<svg width="12" height="12" color="#fff"><use href="#i-search"/></svg></div>
    <div class="btn-new" style="left:658px;top:145px">+ New</div>
    <div class="table" style="left:269px;top:188px;width:876px;height:242px">
      <div class="thead">
        <span class="cell" style="left:17px">Name</span>
        <span class="cell" style="left:281px">Username</span>
        <span class="cell" style="left:544px">Login Page URL</span>
      </div>
      <div class="row" style="top:46px;height:50px">
        <div class="ring" style="left:16px;top:9px"><svg color="var(--blue)"><use href="#i-key"/></svg></div>
        <span class="cell" style="left:70px">exchange.kelvara</span>
        <span class="cell" style="left:281px">my kelvara \ hana_gale</span>
        <span class="cell" style="left:544px">https://exchangekelvara.com</span>
      </div>
      <div class="row" style="top:96px;height:48px">
        <div class="ring" style="left:16px;top:8px"></div>
        <span class="cell" style="left:70px">Chatterly</span>
        <span class="cell" style="left:281px">jmarlow@mailpost.com</span>
        <span class="cell" style="left:544px">https://www.chatterly.com</span>
      </div>
      <div class="row dark" style="top:144px;height:49px">
        <div class="ring" style="left:16px;top:8px"></div>
        <span class="cell" style="left:70px">Repodock</span>
        <span class="cell" style="left:281px">jmarlow@mailpost.com</span>
        <span class="cell" style="left:544px">https://repodock.com/login</span>
        <svg class="cell" style="left:754px" width="13" height="13" color="var(--blue)"><use href="#i-key"/></svg>
        <svg class="cell" style="left:795px" width="13" height="13" color="var(--blue)"><use href="#i-pencil"/></svg>
        <svg class="cell" style="left:835px" width="13" height="13" color="var(--blue)"><use href="#i-trash"/></svg>
      </div>
      <div class="row" style="top:193px;height:48px">
        <div class="ring" style="left:16px;top:8px">i</div>
        <span class="cell" style="left:70px">talentry - default</span>
        <span class="cell" style="left:281px">lena_gale@kelvara.com</span>
        <span class="cell" style="left:544px">https://www.talentry.cn/Login</span>
      </div>
    </div>
    <div class="count">x10</div>
  </div>
</div>

</body>
</html>
```